We need an attractive business card design that is modern and inviting. We like the blue and yellow (or gold) colors that are displayed with the logo. The business should communicate trust, experience, and integrity.

Target Market(s)

Residential and Commercial

Industry/Entity Type

Business

Contact Information for Business Card

Recessed Lighting
LED Retro Fit
Sign Repair
Alarms and Cameras
Mobile Home Services
24hr service calls

Font styles to use
Serif
Sans Serif

Colors
3176b5
0455a3
fece3e
fbee3e

Requirements
Must have
• Brannick Electric
• Owner: Marcus Brannick
• Licensed and Insured
• TECL #58731
Nice to have
• Exquisite Detail!!
• Over 20 years of experience
Should not have
• Nothing boring or traditional!!!

```html
<!DOCTYPE html>
<html lang="en">
<head>
<meta charset="utf-8">
<title>Brannick Electric – Business Card</title>
<link href="https://fonts.googleapis.com/css2?family=Open+Sans:wght@400;600;700;800&display=swap" rel="stylesheet">
<style>
  :root {
    --brand-blue: #0455a3;
    --brand-blue-light: #3176b5;
    --brand-yellow: #fbee3e;
    --ink: #3a3a3a;
    --rule: #4a4a4a;
    --card: #ffffff;
    --ghost: #f1f1f1;
    --backdrop: #e9e7e4;
  }
  * { margin: 0; padding: 0; box-sizing: border-box; }
  html, body { width: 1200px; height: 1000px; overflow: hidden; }
  body {
    background: var(--backdrop);
    font-family: "Open Sans", Arial, sans-serif;
    color: var(--ink);
    position: relative;
  }
  .card {
    position: absolute;
    left: 266px;
    width: 666px;
    height: 398px;
    background: var(--card);
    border-radius: 24px;
    overflow: hidden;
    box-shadow: 0 6px 18px rgba(0,0,0,0.18);
  }
  .card--front { top: 74px; }
  .card--back { top: 533px; }

  .ghost-ring {
    position: absolute;
    border: 34px solid var(--ghost);
    border-radius: 50%;
  }
  .card--front .ghost-ring { left: 474px; top: -10px; width: 300px; height: 300px; }
  .card--back .ghost-ring { left: -20px; top: 6px; width: 340px; height: 340px; }

  .brand-dot {
    width: 84px; height: 84px;
    border: 9px solid var(--brand-blue);
    border-radius: 50%;
  }
  .card--front .brand-dot { position: absolute; left: 126px; top: 31px; }

  .brand-name {
    font-weight: 800;
    font-size: 26px;
    line-height: 36px;
    letter-spacing: 0.4px;
    color: var(--brand-blue);
    white-space: nowrap;
    text-transform: uppercase;
  }
  .card--front .brand-name { position: absolute; left: 31px; top: 123px; }

  .back-brand {
    position: absolute;
    right: 32px; top: 117px;
    width: 300px;
    display: flex; flex-direction: column; align-items: center;
    text-align: center;
  }
  .back-brand .brand-name { margin-top: 4px; }
  .tagline { font-size: 16px; line-height: 24px; margin-top: 2px; }
  .license { font-size: 14px; line-height: 20px; margin-top: 2px; color: var(--brand-blue); font-weight: 600; letter-spacing: 0.3px; }

  .services { position: absolute; left: 32px; top: 212px; }
  .services__title {
    font-size: 16px; font-weight: 700; color: var(--brand-blue);
    letter-spacing: 0.3px;
  }
  .services__rule {
    position: absolute; left: 32px; top: 239px;
    width: 432px; height: 2px; background: var(--rule);
  }
  .services__list { list-style: none; margin-top: 13px; font-size: 16.5px; line-height: 22px; }
  .services__list span::before {
    content: ""; display: inline-block; width: 6px; height: 6px;
    border-radius: 50%; background: var(--brand-blue);
    margin: 0 4px 3px 1px; vertical-align: middle;
  }

  .owner { position: absolute; right: 32px; top: 200px; text-align: right; }
  .owner__name { font-size: 21px; font-weight: 700; color: var(--brand-blue); letter-spacing: 0.3px; line-height: 28px; }
  .owner__role { font-size: 16px; line-height: 22px; }

  .contact { position: absolute; right: 32px; top: 261px; list-style: none; text-align: right; }
  .contact li { font-size: 16px; line-height: 23px; display: flex; justify-content: flex-end; align-items: center; gap: 6px; }
  .contact svg { width: 15px; height: 15px; fill: var(--brand-blue); }

  .band { position: absolute; bottom: 0; height: 20px; }
  .band--blue { left: 0; width: 330px; background: var(--brand-blue); }
  .band--yellow { left: 334px; right: 0; background: var(--brand-yellow); }
</style>
</head>
<body>

<section class="card card--front" aria-label="Card front">
  <div class="ghost-ring"></div>
  <div class="brand-dot"></div>
  <div class="brand-name">Brannick Electric</div>

  <div class="services">
    <h2 class="services__title">SPECIALIZED IN:</h2>
    <ul class="services__list">
      <li><span></span>24hr service calls</li>
      <li><span></span>Residential &amp; Commercial</li>
      <li><span></span>Recessed Lighting <span></span>LED Retro Fit</li>
      <li><span></span>Sign Repair <span></span>Alarms and Cameras</li>
      <li><span></span>Mobile Home Services</li>
    </ul>
  </div>
  <div class="services__rule"></div>

  <div class="owner">
    <div class="owner__name">MARCUS BRANNICK</div>
    <div class="owner__role">Licensed and Insured</div>
  </div>

  <ul class="contact">
    <li>+ 000 000 0000
      <svg viewBox="0 0 16 16" aria-hidden="true"><path d="M1 6c0-2 3-4 7-4s7 2 7 4v1h-4V5.5H5V7H1z"/><path d="M3 8h10l1 6H2z"/></svg></li>
    <li>+ 000 000 0000
      <svg viewBox="0 0 16 16" aria-hidden="true"><path d="M4 1h8v4H4z"/><path d="M1 6h14v6h-3v-2H4v2H1z"/><path d="M5 11h6v4H5z"/></svg></li>
    <li>Info@BrannickElectric.com
      <svg viewBox="0 0 16 16" aria-hidden="true"><path d="M1 3h14v1L8 9 1 4z"/><path d="M1 5.5l7 5 7-5V13H1z"/></svg></li>
    <li>www.BrannickElectric.com
      <svg viewBox="0 0 16 16" aria-hidden="true"><path d="M8 1a7 7 0 1 0 0 14A7 7 0 0 0 8 1zm0 2a5 5 0 0 1 4.6 3H10L8.5 4.5 7 6H5l1-2.6A5 5 0 0 1 8 3zM3.2 7H6l1 2-1.5 3A5 5 0 0 1 3.2 7zm5.3 6 1.5-3.5h3A5 5 0 0 1 8.5 13z"/></svg></li>
  </ul>

  <div class="band band--blue"></div>
  <div class="band band--yellow"></div>
</section>

<section class="card card--back" aria-label="Card back">
  <div class="ghost-ring"></div>
  <div class="back-brand">
    <div class="brand-dot"></div>
    <div class="brand-name">Brannick Electric</div>
    <p class="tagline">Over 20 years of experience</p>
    <p class="license">TECL #58731</p>
  </div>
</section>

</body>
</html>
```